Corrow Family Farm fresh honey jar label

I need a label for jars of honey harvested at our farm. These are for gifts and personal use. We are looking to incorporate our farm brand into the label. We would like the design to take the existing brand and add some element like bees, honey, flowers, or hives to indicate the contents. We want the design to feel homemade and authentic without feeling cheap or hoaky

Requirements
Must have
• The label must be made to fit a 1" x2" rectangular label. The label must include the attached family brand. The label must include the text "Corrow Family Farms" "Pinebrook, USA" "Farm Fresh Honey". The label will be printed on off-white paper
Nice to have
• It would be nice to have illustrations of bees or flowers around the logo or hives or honeycombs. The label should have a vintage feel
Should not have
• The label should not feel overly cartoonish or hoaky

```html
<!DOCTYPE html>
<html lang="en">
<head>
<meta charset="utf-8">
<title>Corrow Family Farms – Farm Fresh Honey Label</title>
<link rel="stylesheet" href="https://fonts.googleapis.com/css2?family=Montserrat:wght@400;600;700&family=Questrial&family=Josefin+Sans:wght@300;400&display=swap">
<style>
  :root {
    --backdrop: #ececec;
    --paper: #fdfcf8;
    --ink: #111111;
    --honey-orange: #e0532a;
    --bee-yellow: #f2b43a;
  }
  html, body {
    margin: 0;
    padding: 0;
    width: 1200px;
    height: 1200px;
    overflow: hidden;
    background: var(--backdrop);
  }
  .canvas {
    position: relative;
    width: 1200px;
    height: 1200px;
  }
  .label {
    position: absolute;
    left: 362px;
    top: 127px;
    width: 475px;
    height: 945px;
    background: var(--paper);
    color: var(--ink);
  }
  .brand-name {
    position: absolute;
    left: 0;
    right: 0;
    top: 96px;
    margin: 0;
    text-align: center;
    font-family: "Montserrat", sans-serif;
    font-weight: 700;
    font-size: 38px;
    line-height: 1.15;
    letter-spacing: 3px;
    color: var(--ink);
  }
  .brand-place {
    position: absolute;
    left: 0;
    right: 0;
    top: 259px;
    margin: 0;
    text-align: center;
    font-family: "Montserrat", sans-serif;
    font-weight: 400;
    font-size: 13px;
    letter-spacing: 0.5px;
  }
  .farm-name {
    position: absolute;
    left: 0;
    right: 0;
    top: 340px;
    margin: 0;
    text-align: center;
    font-family: "Questrial", sans-serif;
    font-size: 27px;
    letter-spacing: 1px;
    text-transform: uppercase;
    color: var(--honey-orange);
  }
  .farm-name .initial {
    font-family: "Montserrat", sans-serif;
    font-weight: 700;
    font-size: 31px;
  }
  .fresh-banner {
    position: absolute;
    left: 62px;
    top: 432px;
    width: 332px;
    height: 100px;
  }
  .fresh-banner text {
    font-family: "Josefin Sans", sans-serif;
    font-weight: 400;
    font-size: 31px;
    letter-spacing: 4px;
    fill: var(--paper);
  }
  .product-name {
    position: absolute;
    left: 0;
    right: 0;
    top: 532px;
    margin: 0;
    text-align: center;
    font-family: "Josefin Sans", sans-serif;
    font-weight: 300;
    font-size: 86px;
    line-height: 1;
    letter-spacing: 4px;
    color: transparent;
    -webkit-text-stroke: 2px var(--honey-orange);
  }
  .bee-art {
    position: absolute;
    left: 140px;
    top: 636px;
    width: 195px;
    height: 175px;
    border-radius: 50%;
    background: radial-gradient(circle at 50% 55%, var(--bee-yellow) 0%, #c98a1e 45%, #f4f1e8 72%, var(--paper) 100%);
  }
  .origin {
    position: absolute;
    left: 0;
    right: 0;
    top: 864px;
    margin: 0;
    text-align: center;
    font-family: "Montserrat", sans-serif;
    font-weight: 600;
    font-size: 24px;
    letter-spacing: 2px;
  }
</style>
</head>
<body>
<main class="canvas">
  <section class="label">
    <h2 class="brand-name">CORROW<br>FAMILY<br>FARM</h2>
    <p class="brand-place">PINEBROOK, LOUISIANA</p>

    <h1 class="farm-name"><span class="initial">C</span>orrow <span class="initial">F</span>amily <span class="initial">F</span>arms</h1>

    <svg class="fresh-banner" viewBox="0 0 332 100" aria-label="Farm Fresh">
      <defs>
        <path id="banner-arc" d="M24,72 Q166,16 308,72"/>
      </defs>
      <path d="M0,40 Q166,-14 332,40 L318,98 Q166,52 14,98 Z" fill="var(--ink)"/>
      <text text-anchor="middle"><textPath href="#banner-arc" startOffset="50%">FARM FRESH</textPath></text>
    </svg>

    <p class="product-name">HONEY</p>

    <div class="bee-art" role="img" aria-label="Illustration of a striped yellow and black honey bee with white wings"></div>

    <p class="origin">PINEBROOK, USA</p>
  </section>
</main>
</body>
</html>
```